Envelope Design - Winner can do follow-up business

- Marvuno.com is a Swiss-based online store selling business shirts and accessories for business men
- Please visit the webpage to make yourself familiar with the company. Although the text is in German, with Google translator you should be able to understand the main content.
- Our clients are mainly business men between 30 and 60 years old. Mostly with a high income working in the service industry (banking, insurance, lawyers, etc.). Sometimes there wives purchase the shirts for them ;-)
- The colors and the logo are given, as they are also used for the print materials (please see files in attachment)
- I am running several businesses and often need a talented web designer --> the winner gets substantial follow-up business
your task:
-for our company we need a new envelope design
-It should be simple and modern
-please use one of the logos in the followings.
-suprise me :)

```html
<!DOCTYPE html>
<html lang="en">
<head>
<meta charset="utf-8">
<title>Marvuno Envelope</title>
<link rel="stylesheet" href="https://fonts.googleapis.com/css2?family=Michroma&display=swap">
<style>
  :root {
    --page: #ffffff;
    --paper: #ffffff;
    --edge: #b9b9b9;
    --fold: #b5b5b5;
    --gold: #e2d46a;
    --red: #e8392e;
  }
  html, body {
    margin: 0;
    padding: 0;
    overflow: hidden;
    background: var(--page);
  }
  .canvas {
    position: relative;
    width: 1191px;
    height: 1200px;
    overflow: hidden;
    background: var(--page);
    font-family: "Michroma", "Arial", sans-serif;
  }
  .envelope {
    position: absolute;
    width: 689px;
    height: 346px;
    background: var(--paper);
    border: 1px solid var(--edge);
    box-shadow: 6px 14px 26px rgba(0, 0, 0, 0.22);
    box-sizing: border-box;
  }
  .envelope--front { left: 255px; top: 152px; }
  .envelope--back  { left: 251px; top: 684px; }

  .brand {
    position: absolute;
    display: flex;
    align-items: center;
    gap: 10px;
    color: var(--gold);
    font-size: 24px;
    letter-spacing: 1px;
    line-height: 1;
    white-space: nowrap;
  }
  .brand__mark {
    width: 18px;
    height: 18px;
    background: var(--red);
    flex: none;
  }
  .brand--corner { top: 26px; right: 26px; }
  .brand--margin { left: 24px; bottom: 30px; font-size: 18px; }
  .brand--flap {
    left: 50%;
    top: 128px;
    transform: translateX(-50%);
    flex-direction: column;
    gap: 14px;
  }
  .brand--flap .brand__mark {
    width: 44px;
    height: 44px;
    background: var(--gold);
  }
  .flap-line {
    position: absolute;
    left: 0;
    top: 0;
    width: 100%;
    height: 100%;
  }
</style>
</head>
<body>
<main class="canvas">
  <section class="envelope envelope--front" aria-label="Envelope front">
    <div class="brand brand--corner"><span>MARVUNO</span><span class="brand__mark"></span></div>
    <div class="brand brand--margin"><span class="brand__mark"></span><span>MARVUNO</span></div>
  </section>

  <section class="envelope envelope--back" aria-label="Envelope back">
    <svg class="flap-line" viewBox="0 0 689 346" preserveAspectRatio="none" aria-hidden="true">
      <polyline points="0,95 344,191 689,97" fill="none" stroke="var(--fold)" stroke-width="1.2"/>
    </svg>
    <div class="brand brand--flap"><span class="brand__mark"></span><span>MARVUNO</span></div>
  </section>
</main>
</body>
</html>
```